(4) Bowling League Designs 1920x1080

Will be used on our website and in some digital signage.

We are starting (4) leagues this summer and need a basic graphic as an attention grab which will then lead the customer to full information / sign ups. The information I would need on each one is as follows:

1. Monday Night FREE ball league - Begins May 3rd

2. Tuesday Trios - KFDL Sanctioned - Begins May 11th
$9,000 prize fund

3. Wednesday Cosmic League - 9 pin no tap fun league - May 12th start

4. Thursday Night FREE ball league - Begins May 13th

I will attach some random examples of previous ones to give you an idea.

```html
<!DOCTYPE html>
<html lang="en">
<head>
<meta charset="utf-8">
<title>Monday Night Free Ball League</title>
<link rel="stylesheet" href="https://fonts.googleapis.com/css2?family=Barlow+Condensed:ital,wght@1,600;1,700;1,800;1,900&display=swap">
<style>
  :root {
    --bg-deep: #03110c;
    --bg-glow: #0f7a5a;
    --mint: #43f0a0;
    --mint-soft: #5ef5b8;
    --white: #ffffff;
    --photo-mid: #1fa86e;
  }
  * { margin: 0; padding: 0; box-sizing: border-box; }
  html, body { width: 1200px; height: 675px; overflow: hidden; background: var(--bg-deep); }
  .poster {
    position: relative; width: 1200px; height: 675px; overflow: hidden;
    background:
      radial-gradient(ellipse 420px 260px at 300px 300px, rgba(30,200,150,0.5), transparent 70%),
      radial-gradient(ellipse 500px 200px at 450px 60px, rgba(20,160,120,0.45), transparent 70%),
      linear-gradient(90deg, #020806 0%, #083a2b 40%, var(--bg-glow) 60%, #0a4a34 100%);
    font-family: "Barlow Condensed", sans-serif;
  }
  .hero-photo {
    position: absolute; left: 530px; top: 0; width: 670px; height: 675px;
    background:
      radial-gradient(ellipse 260px 320px at 330px 380px, rgba(230,250,245,0.85), rgba(143,232,200,0.5) 55%, transparent 80%),
      radial-gradient(circle 520px at 620px 480px, rgba(60,220,120,0.6), transparent 70%),
      linear-gradient(90deg, transparent 0%, var(--photo-mid) 35%, #0c5a3c 100%);
  }
  .frame { position: absolute; border-radius: 4px; }
  .frame--outer3 { left: 10px; top: 198px; width: 552px; height: 230px; border: 2px solid rgba(255,255,255,0.08); }
  .frame--outer2 { left: 34px; top: 206px; width: 488px; height: 208px; border: 3px solid rgba(255,255,255,0.14); }
  .frame--outer1 { left: 58px; top: 214px; width: 442px; height: 192px; border: 3px solid rgba(255,255,255,0.3); }
  .frame--main {
    left: 75px; top: 225px; width: 400px; height: 169px;
    border: 3px solid var(--white); border-radius: 6px;
    box-shadow: 0 0 14px rgba(120,255,210,0.9), inset 0 0 14px rgba(120,255,210,0.6);
  }
  .rule { position: absolute; height: 4px; background: var(--mint-soft); box-shadow: 0 0 8px var(--mint); }
  .rule--upper { left: 275px; top: 440px; width: 365px; }
  .rule--lower { left: 0; top: 504px; width: 178px; }
  .date-box, .date-tick {
    position: absolute; top: 558px; height: 58px;
    border: 2px solid var(--white); border-radius: 6px;
    box-shadow: 0 0 10px rgba(120,255,210,0.8);
  }
  .date-box { left: 75px; width: 388px; }
  .date-tick--1 { left: 470px; width: 29px; }
  .date-tick--2 { left: 511px; width: 29px; }
  .date-tick--3 { left: 552px; width: 34px; }
  .type-layer { position: absolute; left: 0; top: 0; width: 1200px; height: 675px; }
  .type-layer text { font-family: "Barlow Condensed", sans-serif; font-style: italic; }
  .t-day { fill: var(--mint); font-weight: 800; font-size: 80px; }
  .t-night { fill: var(--white); font-weight: 800; font-size: 80px; }
  .t-free { fill: none; stroke: var(--white); stroke-width: 3px; font-weight: 900; font-size: 174px; filter: drop-shadow(0 0 6px rgba(120,255,210,0.9)); }
  .t-bal { fill: var(--white); font-weight: 800; font-size: 67px; }
  .t-l { fill: var(--mint); font-weight: 800; font-size: 125px; }
  .t-eague { fill: var(--white); font-weight: 800; font-size: 76px; }
  .t-date { fill: var(--white); font-weight: 700; font-size: 40px; }
  .chevron { fill: var(--mint); }
</style>
</head>
<body>
  <main class="poster">
    <div class="hero-photo" role="img" aria-label="Photo of white bowling pins with red stripes scattering as a black bowling ball strikes them, green glowing rings behind"></div>

    <div class="frame frame--outer3"></div>
    <div class="frame frame--outer2"></div>
    <div class="frame frame--outer1"></div>
    <div class="frame frame--main"></div>

    <div class="rule rule--upper"></div>
    <div class="rule rule--lower"></div>

    <div class="date-box"></div>
    <div class="date-tick date-tick--1"></div>
    <div class="date-tick date-tick--2"></div>
    <div class="date-tick date-tick--3"></div>

    <svg class="type-layer" viewBox="0 0 1200 675">
      <polygon class="chevron" points="37,66 78,84.5 37,103 46,84.5"/>
      <polygon class="chevron" points="37,434 78,452.5 37,471 46,452.5"/>
      <text class="t-day" x="97" y="116" textLength="272" lengthAdjust="spacingAndGlyphs">MONDAY</text>
      <text class="t-night" x="97" y="194" textLength="198" lengthAdjust="spacingAndGlyphs">NIGHT</text>
      <text class="t-free" x="110" y="369" textLength="330" lengthAdjust="spacingAndGlyphs">FREE</text>
      <text class="t-bal" x="94" y="484" textLength="115" lengthAdjust="spacingAndGlyphs">BAL</text>
      <text class="t-l" x="212" y="519" textLength="42" lengthAdjust="spacingAndGlyphs">L</text>
      <text class="t-eague" x="258" y="519" textLength="208" lengthAdjust="spacingAndGlyphs">EAGUE</text>
      <text class="t-date" x="162" y="600" textLength="216" lengthAdjust="spacingAndGlyphs">Begins May 3rd</text>
    </svg>
  </main>
</body>
</html>
```